Business card design for strategy and management consulting company. Would like to have a clean and professional business card, based on the attached logo. The company is a strategy and management consulting company focusing on sustainable business modlels based on economic, social and environmental market opportunities. Preferably the logo should be included on both sides of the design.

Industry/Entity Type

Business

Contact Information for Business Card

Håvard Lilleby, CEO/Management consultant
havard.lilleby@quarvenpartners.example
Mob: +47 948 26 317
Office: Vikfjell gate 14, pb 312 sentrum, N-0172 Oslo Norway

Requirements
Must have
• Include attached logo
Nice to have
• Would like to have the logo on both sides
Should not have
• Many colours.

```html
<!DOCTYPE html>
<html lang="en">
<head>
<meta charset="UTF-8">
<title>Quarven business card</title>
<link rel="stylesheet" href="https://fonts.googleapis.com/css2?family=Montserrat:wght@400;600;700&display=swap">
<style>
  :root {
    --backdrop: #e9e9e7;
    --ink: #111111;
    --charcoal: #2b2b2b;
    --paper: #f4f4f2;
    --signal: #f7e21b;
    --muted: #7a7a7a;
    --white: #ffffff;
  }
  * { margin: 0; padding: 0; box-sizing: border-box; }
  html, body {
    width: 1200px; height: 1000px; overflow: hidden;
    background: var(--backdrop);
    font-family: "Montserrat", Arial, sans-serif;
  }
  .sheet {
    width: 1200px; height: 1000px;
    display: flex; flex-direction: column; align-items: center; justify-content: center;
    gap: 60px;
  }
  .card {
    position: relative;
    width: 700px; height: 400px;
    overflow: hidden;
    box-shadow: 0 10px 30px rgba(0,0,0,0.18);
  }
  .wordmark {
    position: absolute; left: 0; right: 0;
    text-align: center;
    font-weight: 600; letter-spacing: -1px; line-height: 1;
  }
  /* Front */
  .card--front {
    background: linear-gradient(160deg, #2a2a2a 0%, var(--ink) 55%, #050505 100%);
  }
  .card--front .wordmark {
    top: 150px; color: var(--white); font-size: 84px;
  }
  .card--front .accent-band {
    position: absolute; left: 0; right: 0; bottom: 0; height: 22px;
    background: var(--signal);
  }
  /* Back */
  .card--back { background: var(--paper); }
  .card--back .accent-band {
    position: absolute; left: 0; right: 0; top: 0; height: 14px;
    background: var(--signal);
  }
  .card--back .wordmark {
    top: 72px; color: var(--ink); font-size: 64px;
  }
  .contact-row {
    position: absolute; left: 0; right: 0; top: 190px;
    display: flex; justify-content: center; align-items: center; gap: 22px;
  }
  .identity { text-align: right; }
  .identity .name { font-weight: 700; font-size: 18px; color: var(--ink); }
  .identity .role { font-size: 14px; color: var(--muted); margin-top: 4px; }
  .divider { width: 2px; height: 50px; background: #9a9a9a; }
  .channels { list-style: none; font-size: 14px; color: var(--ink); }
  .channels li { display: flex; align-items: center; gap: 7px; line-height: 1.6; }
  .channels svg { width: 13px; height: 13px; flex: none; }
  .address-band {
    position: absolute; left: 0; right: 0; bottom: 0; height: 92px;
    background: var(--charcoal);
  }
  .address-band .address {
    position: absolute; left: 0; right: 0; top: 24px; text-align: center;
    color: var(--white); font-weight: 600; font-size: 14px; letter-spacing: 0.2px;
  }
  .address-band .address-rule {
    position: absolute; left: 120px; right: 80px; top: 52px; height: 10px;
    background: var(--signal);
  }
</style>
</head>
<body>
<main class="sheet">
  <section class="card card--front" aria-label="Card front">
    <p class="wordmark">Quarven</p>
    <div class="accent-band"></div>
  </section>

  <section class="card card--back" aria-label="Card back">
    <div class="accent-band"></div>
    <p class="wordmark">Quarven</p>
    <div class="contact-row">
      <div class="identity">
        <p class="name">Håvard Lilleby</p>
        <p class="role">CEO/Management Consultant</p>
      </div>
      <div class="divider"></div>
      <ul class="channels">
        <li>
          <svg viewBox="0 0 16 16" aria-hidden="true"><circle cx="8" cy="8" r="8" fill="#111"/><path d="M5.2 4.2l1.5 1.6-.8 1c.5 1.1 1.2 1.8 2.3 2.3l1-.8 1.6 1.5-.9 1.2C7.3 11 5 8.7 4 6.1z" fill="#fff"/></svg>
          +47 948 26 317
        </li>
        <li>
          <svg viewBox="0 0 16 16" aria-hidden="true"><rect x="1" y="3" width="14" height="10" fill="none" stroke="#111" stroke-width="1.6"/><path d="M1.5 3.5L8 9l6.5-5.5" fill="none" stroke="#111" stroke-width="1.6"/></svg>
          havard.lilleby@quarvenpartners.example
        </li>
      </ul>
    </div>
    <div class="address-band">
      <p class="address">Vikfjell gate 14, pb 312 sentrum, N-0172 Oslo Norway</p>
      <div class="address-rule"></div>
    </div>
  </section>
</main>
</body>
</html>
```